Pendleworth Real Estate Partners Looking For FUNNY, SEXY & KICK ASS Billboards!

We are launching our billboard campaign Jan 2021 and will need 8 billboards. We have some hilarious ideas but need a professional to help us! We are a male and female based real estate partnership selling commercial and residential properties in New Brunswick Canada. We have a lot of ideas but need direction.

Target Market(s)

Sellers and Buyers of Real Estate

Industry/Entity Type

Real Estate Agent

Font styles to use
Serif

Colors

Designer to choose only greyscale colors for use in the design.

Requirements
Must have
• Funny, sassy and eye-catching. We like to have fun and want out billboards to make people smile.
Nice to have
• Movies references having to do with real estate (we have ideas) WE would like the project to be cohesive over the 8 billboards.
Should not have
• Too much colour or too generic. We have our brand colours we would like to stick with. Black, white and red accent.

```html
<!DOCTYPE html>
<html lang="en">
<head>
<meta charset="utf-8">
<title>We Want Your Listing – Billboard</title>
<link href="https://fonts.googleapis.com/css2?family=Montserrat:wght@300;400;500;700;800&display=swap" rel="stylesheet">
<style>
  :root {
    --page-bg: #f2f2f2;
    --board-bg: #2f2f2f;
    --board-bg-light: #444444;
    --white: #ffffff;
    --red: #e12a36;
    --rule: #d9d9d9;
    --skin: #e2a27a;
    --skin-soft: #c98e6c;
  }
  * { box-sizing: border-box; margin: 0; padding: 0; }
  html, body {
    width: 889px; height: 1200px; overflow: hidden;
    background: var(--page-bg);
    font-family: "Montserrat", sans-serif;
  }
  .billboard {
    position: absolute; left: 35px; top: 395px;
    width: 820px; height: 410px; overflow: hidden;
    background: radial-gradient(ellipse at 70% 40%, var(--board-bg-light) 0%, var(--board-bg) 65%);
    box-shadow: 0 3px 8px rgba(0,0,0,0.25);
    color: var(--white);
  }
  .hands-photo {
    position: absolute; left: 527px; top: 0; width: 293px; height: 410px;
    background: linear-gradient(120deg, rgba(47,47,47,0) 25%, var(--skin-soft) 60%, var(--skin) 100%);
    opacity: 0.85;
  }
  .brand {
    position: absolute; left: 35px; top: 20px; height: 54px;
    display: flex; align-items: center; gap: 8px;
    font-weight: 700; font-size: 18px; letter-spacing: 0.5px; color: var(--white);
  }
  .brand-square { width: 14px; height: 14px; background: var(--red); }
  .headline { position: absolute; left: 37px; top: 94px; line-height: 1; }
  .headline-light { display: block; font-weight: 300; font-size: 58px; letter-spacing: 1px; }
  .headline-bold { display: block; font-weight: 800; font-size: 58px; color: var(--red); margin-top: 0; letter-spacing: -0.5px; }
  .divider { position: absolute; left: 38px; top: 216px; width: 446px; height: 1px; background: var(--rule); }
  .divider-accent { position: absolute; left: 57px; top: 214px; width: 62px; height: 5px; border-radius: 3px; background: var(--red); }
  .tagline { position: absolute; left: 37px; top: 236px; font-weight: 800; font-size: 23px; line-height: 1.1; letter-spacing: 0.5px; }
  .subline { position: absolute; left: 37px; top: 296px; font-weight: 300; font-size: 18px; }
  .call { position: absolute; left: 37px; top: 328px; font-weight: 800; font-size: 33px; letter-spacing: 0.5px; }
  .call-label { color: var(--red); }
  .contacts {
    position: absolute; left: 37px; top: 373px;
    display: flex; gap: 14px; font-size: 9.5px; font-weight: 500; line-height: 1.3;
  }
  .contact { display: flex; gap: 6px; align-items: flex-start; }
  .contact svg { flex: none; margin-top: 1px; }
</style>
</head>
<body>
  <section class="billboard">
    <div class="hands-photo" role="img" aria-label="Photo of a hand dangling a house key above another open hand holding a small wooden model house"></div>

    <div class="brand"><span class="brand-square"></span>CROWNMARK REALTY</div>

    <h1 class="headline">
      <span class="headline-light">WE WANT</span>
      <span class="headline-bold">YOUR LISTING</span>
    </h1>

    <div class="divider"></div>
    <div class="divider-accent"></div>

    <p class="tagline">THERE'S A NEW SHERIFF<br>IN TOWN</p>
    <p class="subline">This could be us, but you're renting....</p>

    <p class="call"><span class="call-label">CALL NOW</span> (506) 555-0147</p>

    <div class="contacts">
      <div class="contact">
        <svg width="8" height="11" viewBox="0 0 8 11"><path d="M4 0a4 4 0 0 0-4 4c0 3 4 7 4 7s4-4 4-7a4 4 0 0 0-4-4zm0 5.5A1.5 1.5 0 1 1 4 2.5a1.5 1.5 0 0 1 0 3z" fill="#e12a36"/></svg>
        <span>Crownmark Atlantic 48 Harbour Lane<br>Westbay, NB, E2K 1A1</span>
      </div>
      <div class="contact">
        <svg width="10" height="10" viewBox="0 0 10 10" fill="none" stroke="#e12a36" stroke-width="1"><circle cx="5" cy="5" r="4.4"/><ellipse cx="5" cy="5" rx="2" ry="4.4"/><path d="M0.6 5h8.8M1.5 2.8h7M1.5 7.2h7"/></svg>
        <span>www.pendleworthrealestate.ca</span>
      </div>
      <div class="contact">
        <svg width="11" height="8" viewBox="0 0 11 8"><rect width="11" height="8" rx="1" fill="#e12a36"/><path d="M0.5 0.8 5.5 4.6 10.5 0.8" fill="none" stroke="#2f2f2f" stroke-width="1"/></svg>
        <span>jharlow@crownmarkrealty.ca</span>
      </div>
    </div>
  </section>
</body>
</html>
```